Werbe-Email-Design
Zielgruppe
Wir sind Dienstleister in der Industrie/ Automobilindustrie. Die Zielgruppe für unsere Werbe-Email sind potenzielle Kunden (möglichst Einkäufer) für unser Produkt (Motorhersteller für DC-Motoren). Da es sich um eine Werbe-Email handelt, soll beim Öffnen möglichst gleich ersichtlich sein, ob das Produkt für den Empfänger brauchbar ist, sodass er in diesem Falle die 'nervige Werbe-Mail' nicht sofort löscht.
Aufgabenstellung
Bei dem 'Newsletter' soll es sich um eine einmalige Werbemail handeln, durch die potenzielle Kunden auf unser Produkt aufmerksam werden und mit uns in Kontakt treten, unsere Website besuchen oder sofort bestellen.
Das Produkt verfolgt einen eher ungewöhnlichen Ansatz, der den potenziellen Kunden eben ansprechen könnte oder nicht, da er damit selbst ein umfangreicheres Produkt anbieten könnte, sollte das in seinem Interesse sein.
Da dies ein neuer Ansatz für den potenziellen Kunden wäre, wird der Empfänger der Email nicht damit rechnen. Deshalb ist wichtig, dass beim Öffnen der Email sofort klar wird, was unser Produkt bietet und wie es unserem Kunden von Nutzen sein kann.
Es handelt sich bei den potenziellen Kunden um Motorhersteller (für DC-Motoren im Fahrzeug, bspw. Fensterheber), die diesen Motor selbst nicht ansteuern. Sie verkaufen diese Motoren also entweder ohne Steuerung oder kaufen die Steuerung von einem Dienstleister. Wir bieten eben diese Steuerung an, allerdings konfigurierbar auf die Anwendung des Kunden, sodass kein weiterer Entwicklungsaufwand entsteht. Der Kunde kann also entweder einen bestehenden Lieferanten für seine Steuerung durch uns ersetzen, da wir in der Lage sind, einen sehr niedrigen Stückpreis zu bieten, oder sein Geschäftsfeld erweitern.
Durch die Email soll sich der Empfänger um diesen Umstand und die Vorteile, die durch unser Produkt für ihn entstehen, bewusstwerden.
Beim Öffnen der Email soll der 'Eye-Catcher'-Bereich zu sehen sein, der den Kunden neugierig machen soll. Hat der Kunde Interesse, soll bei Scrollen mehr Information zu sehen sein.
Dieser 'Eye-Catcher'-Bereich ist in der anhängenden PowerPoint-Datei auf der ersten Seite enthalten. Beim Scrollen sollen die Informationen, die sich auf den nächsten Seiten befinden, zu sehen sein. Des Weiteren soll ein Foto der geöffneten ECU (anhängend) zu sehen sein, mit den Informationen zum Gehäuse, sowie zwei Screenshots der mitgelieferten GUI. Da ..

```html
<!DOCTYPE html>
<html lang="de">
<head>
<meta charset="utf-8">
<title>Kestrel Antriebstechnik – ECU für DC-Motoren</title>
<link href="https://fonts.googleapis.com/css2?family=Lato:wght@400;700;900&family=Poppins:wght@400;500;600&display=swap" rel="stylesheet">
<style>
  :root{
    --page:#efefef;
    --card:#ffffff;
    --orange:#f7941d;
    --blue:#0a2bc4;
    --blue-text:#1a2fb8;
    --ink:#222222;
    --shade:#d9d9d9;
  }
  *{margin:0;padding:0;box-sizing:border-box}
  html,body{width:1200px;height:2247px;overflow:hidden}
  body{background:var(--page);position:relative;font-family:'Lato',sans-serif;color:var(--ink)}

  .masthead{position:absolute;left:0;top:0;width:1200px;height:190px;background:var(--card);
    display:flex;flex-direction:column;align-items:center;justify-content:center;gap:6px}
  .brand-name{font-family:'Lato',sans-serif;font-weight:900;font-size:58px;color:var(--orange);letter-spacing:1px;display:flex;align-items:center;gap:14px}
  .brand-name .dot{width:22px;height:22px;background:var(--blue);border-radius:50%}
  .brand-sub{font-family:'Lato',sans-serif;font-weight:900;font-size:30px;color:var(--orange)}

  .card{position:absolute;left:24px;width:1152px;background:var(--card);border-radius:12px}

  .advantages{top:256px;height:661px}
  .col{position:absolute;top:36px}
  .col h2{font-weight:900;font-size:24px;line-height:31px;color:var(--orange);text-align:center;letter-spacing:.5px}
  .col .rule{width:178px;height:1px;background:var(--orange);margin:16px auto 22px}
  .col-tech{left:42px;width:320px}
  .col-strat{left:795px;width:330px}
  .col-tech .rule{background:#bbb}

  .list{list-style:none;font-size:18px;line-height:34.5px}
  .list>li{position:relative;padding-left:21px}
  .list>li::before{content:"";position:absolute;left:2px;top:14px;width:7px;height:7px;border-radius:50%;background:var(--orange)}
  .list ul{list-style:none}
  .list ul li{position:relative;padding-left:27px}
  .list ul li::before{content:"";position:absolute;left:6px;top:13px;width:8px;height:8px;border-radius:50%;border:1.5px solid var(--orange)}

  .quickstart{position:absolute;left:408px;top:242px;width:384px;height:691px;background:var(--blue);
    box-shadow:0 12px 30px rgba(0,0,0,.25);color:#fff;padding:38px 30px 0 38px}
  .quickstart h2{font-weight:700;font-size:24px;line-height:31px;text-align:center}
  .quickstart .rule{width:178px;height:2px;background:#fff;margin:12px auto 22px}
  .quickstart ul{list-style:none;font-size:17.5px;line-height:34.5px;font-weight:700}
  .quickstart li{position:relative;padding-left:22px}
  .quickstart li::before{content:"";position:absolute;left:2px;top:14px;width:7px;height:7px;border-radius:50%;background:#fff}
  .quickstart li span{font-weight:400}
  .quickstart li b{font-weight:900}

  .applications{top:962px;height:390px}
  .applications p{position:absolute;left:60px;top:64px;width:600px;font-family:'Poppins',sans-serif;font-weight:600;
    font-size:23px;line-height:42px;color:var(--orange);text-align:center}
  .ecu-photo{position:absolute;left:706px;top:34px;width:412px;height:322px;
    background:linear-gradient(160deg,#aeb3b4 0%,#3a3f40 45%,#5d6b4f 70%,#a8afae 100%)}

  .usage{top:1374px;height:210px}
  .ticks{position:absolute;top:30px;list-style:none;font-family:'Poppins',sans-serif;font-weight:600;font-size:24px;line-height:45px;color:var(--blue-text)}
  .ticks li{display:flex;align-items:center;gap:14px}
  .ticks svg{width:20px;height:16px;flex:none}
  .ticks-left{left:54px}
  .ticks-right{left:573px}

  .details{top:1606px;height:616px;font-family:'Poppins',sans-serif}
  .details h3{font-weight:500;font-size:27px;color:var(--orange);margin-left:55px}
  .details .savings{margin-top:32px}
  .details .housing{margin-top:30px}
  .details ul{list-style:none;font-size:21px;line-height:36px;color:var(--ink);margin:6px 40px 0 55px}
  .details li{position:relative}
  .details li::before{content:"";position:absolute;left:-20px;top:15px;width:7px;height:7px;border-radius:50%;background:var(--orange)}
</style>
</head>
<body>

<header class="masthead">
  <div class="brand-name"><span class="dot"></span>Kestrel</div>
  <div class="brand-sub">Kestrel Antriebstechnik</div>
</header>

<section class="card advantages">
  <div class="col col-tech">
    <h2>TECHNISCHE<br>VORTEILE</h2>
    <div class="rule"></div>
    <ul class="list">
      <li>Dank Halbleitertechnologie gegenüber Relais:
        <ul>
          <li>Leiser</li>
          <li>Kein Verschleiß (Kontaktprellen, Lichtbogenentwicklung), kein Icing</li>
          <li>Sehr präzises Ansprechverhalten</li>
        </ul>
      </li>
      <li>Hohe Dynamik im Lastbereich: bis 19A (Stromspitzen bis 30A)</li>
      <li>Geringer Stromverbrauch:
        <ul>
          <li>Sleep-Mode: &lt; 100 µA.</li>
          <li>On-Mode: &lt; 100 mA</li>
        </ul>
      </li>
      <li>Robust gegen Umwelteinflüsse</li>
    </ul>
  </div>

  <div class="col col-strat">
    <h2>STRATEGISCHE<br>VORTEILE</h2>
    <div class="rule"></div>
    <ul class="list">
      <li>Komplettpaket zur Ermittlung Ihrer Systemparameter (Strom-/ Spannungsschwellen, Timingparameter u.v.m.)</li>
      <li>ECU bewährt seit 2010</li>
      <li>HW-Stand 3. Generation</li>
      <li>Zertifiziert nach ...</li>
      <li>Keine Basisentwicklung erforderlich</li>
      <li>Minimaler Aufwand bei Applikation durch GUI-Konfigurator</li>
      <li>Made in Germany</li>
      <li>Schneller geht’s nicht</li>
    </ul>
  </div>
</section>

<aside class="quickstart">
  <h2>IN WENIGEN TAGEN<br>ZUR FERTIGEN</h2>
  <div class="rule"></div>
  <ul>
    <li><span>Ermitteln Sie Ihre Systemparameter mit unserem</span> <b>Komplettpaket</b> <span>zum Anschluss an</span> <b>Ihren DC-Motor</b></li>
    <li><span>Per einfachem Mausklick werden Ihre Parameter in unsere</span> <b>fertige Software</b> <span>geladen</span></li>
    <li><span>Sie können Ihre Einstellungen innerhalb</span> <b>weniger Minuten testen</b><span>, bis Sie mit unserer maßgeschneiderten Lösung zufrieden sind</span></li>
    <li><span>Wir erstellen das LIN File für Ihre Kommunikation mit dem System Ihres Kunden</span></li>
    <li><span>Die</span> <b>fertige ECU</b> <span>ist bereit für Ihre Bestellung</span></li>
  </ul>
</aside>

<section class="card applications">
  <p>Fensterheber | elektrisch verstellbare Spiegel | Schiebedach | elektrische Sitzverstellung | Scheibenwischer&nbsp; Waschwasserpumpen | Türverriegelung | Spoilerverstellung | Beschattungssysteme | elektrischer Heckklappenantrieb</p>
  <div class="ecu-photo" role="img" aria-label="Foto der geöffneten ECU: grüne Platine in schwarzem Kunststoffgehäuse"></div>
</section>

<section class="card usage">
  <ul class="ticks ticks-left">
    <li><svg viewBox="0 0 20 16"><path d="M2 8.5 7.5 14 18 2.5" fill="none" stroke="currentColor" stroke-width="3.5"/></svg>Anwendung</li>
    <li><svg viewBox="0 0 20 16"><path d="M2 8.5 7.5 14 18 2.5" fill="none" stroke="currentColor" stroke-width="3.5"/></svg>für DC Bürstenmotoren</li>
    <li><svg viewBox="0 0 20 16"><path d="M2 8.5 7.5 14 18 2.5" fill="none" stroke="currentColor" stroke-width="3.5"/></svg>in einer LIN-Umgebung</li>
  </ul>
  <ul class="ticks ticks-right">
    <li><svg viewBox="0 0 20 16"><path d="M2 8.5 7.5 14 18 2.5" fill="none" stroke="currentColor" stroke-width="3.5"/></svg>bei hohem Lastbereich</li>
    <li><svg viewBox="0 0 20 16"><path d="M2 8.5 7.5 14 18 2.5" fill="none" stroke="currentColor" stroke-width="3.5"/></svg>mit schnellen Schaltzeiten</li>
    <li><svg viewBox="0 0 20 16"><path d="M2 8.5 7.5 14 18 2.5" fill="none" stroke="currentColor" stroke-width="3.5"/></svg>präzisen Positionsinformationen.</li>
  </ul>
</section>

<section class="card details">
  <h3 class="savings">Mit unserer ECU sparen Sie Kosten, da</h3>
  <ul>
    <li>wir aufgrund eines langjährigen Skaleneffekts einen niedrigen Stückpreis anbieten</li>
    <li>Keine Entwicklungskosten entstehen</li>
    <li>für Sie kaum Aufwand bei der Konfiguration entsteht – unser Entwicklungstool mit Realtime Strom- und Spannungsmessung erleichtert die schnelle Applikation</li>
    <li>Sie von uns ein kostenloses Konfigurationspaket zur Verfügung gestellt bekommen – es fallen für Sie bis zur Bestellung keine Kosten an!</li>
  </ul>
  <h3 class="housing">Gehäuse</h3>
  <ul>
    <li>12-poliger Vantor-Stecker</li>
    <li>2-Komponenten Vergusstechnologie auf Silikonbasis</li>
    <li>IP53</li>
    <li>Material: PA6-GF15</li>
    <li>Einfaches Clip-System zur Befestigung</li>
    <li>Alternatives Gehäuse auf Anfrage</li>
  </ul>
</section>

</body>
</html>
```